Startup internet service provider needs a good facebook ad

Looking for a catchy facebook ad to launch our internet service in Parker, Colorado. Short video or slideshow preferred, still pictures are okay.

https://www.facebook.com/BrimcoreNetworks

www.brimcore-networks.example

Target Market(s)

Parker Colorado

Colors
add136
0255a3

```html
<!DOCTYPE html>
<html lang="en">
<head>
<meta charset="utf-8">
<title>Brimcore Networks – Ultra High Speed Internet</title>
<link rel="stylesheet" href="https://fonts.googleapis.com/css2?family=Archivo+Black&family=Arimo:wght@700&family=Open+Sans:ital,wght@0,400;0,600;1,400;1,700;1,800&family=Oswald:wght@400&display=swap">
<style>
  :root {
    --brand-green: #add136;
    --brand-blue: #0255a3;
    --ink-dark: #2a2a2a;
    --ink-brown: #3b2a20;
    --white: #ffffff;
    --hero-deep: #06122a;
    --hero-cyan: #1aa3e0;
    --essential: #f08a1c;
    --basic: #6fb52c;
    --premier: #9b3aa6;
    --price-grey: #8a8a8a;
    --city-deep: #0b1424;
  }
  * { box-sizing: border-box; margin: 0; padding: 0; }
  html, body { width: 768px; height: 1200px; overflow: hidden; background: var(--white); }
  .ad { position: relative; width: 768px; height: 1200px; overflow: hidden; font-family: "Open Sans", sans-serif; }

  .hero-photo {
    position: absolute; left: 0; top: 0; width: 768px; height: 392px;
    background:
      radial-gradient(ellipse 260px 120px at 60% 8%, rgba(120,80,60,.55), transparent 70%),
      radial-gradient(ellipse 420px 180px at 35% 72%, rgba(26,163,224,.85), transparent 70%),
      radial-gradient(ellipse 300px 140px at 80% 60%, rgba(40,120,220,.7), transparent 70%),
      linear-gradient(180deg, #1a1410 0%, #0a2550 45%, #0b4f93 75%, var(--hero-deep) 100%);
  }
  .headline {
    position: absolute; right: 68px; top: 38px; text-align: right;
    color: var(--white); font-style: italic; font-weight: 800;
    font-size: 62px; line-height: 68px; letter-spacing: -1px;
    text-shadow: 0 2px 6px rgba(0,0,0,.5);
  }
  .chevrons-red { position: absolute; left: 634px; top: 62px; width: 96px; height: 64px; }
  .chevrons-light { position: absolute; left: 340px; top: 180px; width: 230px; height: 56px; }

  .tick-badge { position: absolute; left: 12px; top: 288px; width: 174px; height: 174px; }
  .tagline-hero {
    position: absolute; left: 190px; top: 330px; color: var(--white);
    font-style: italic; font-weight: 700; font-size: 28px; letter-spacing: -.5px;
    text-shadow: 0 2px 4px rgba(0,0,0,.5);
  }

  .middle-band {
    position: absolute; left: 0; top: 392px; width: 768px; height: 322px;
    background: linear-gradient(180deg, #ffffff 0%, #ffffff 48%, #b8d0ea 70%, #4f86c6 88%, #1b5cab 100%);
  }
  .people-photo {
    position: absolute; left: 342px; top: 392px; width: 426px; height: 322px;
    background:
      radial-gradient(ellipse 140px 90px at 30% 20%, rgba(90,110,140,.35), transparent 70%),
      radial-gradient(ellipse 160px 110px at 70% 85%, rgba(60,90,130,.35), transparent 70%),
      linear-gradient(160deg, #f1e6d8 0%, #e2cdb4 50%, #c9ad8e 100%);
    opacity: .92;
  }
  .benefit-list {
    position: absolute; left: 32px; top: 480px; list-style: none;
    color: var(--ink-dark); font-size: 17px; line-height: 27px;
  }
  .benefit-list li::before { content: "– "; }

  .package-title {
    position: absolute; left: 420px; top: 424px; width: 336px; text-align: center;
    color: var(--ink-brown); font-family: "Arimo", sans-serif; font-weight: 700;
    font-size: 24px; line-height: 37px; letter-spacing: .5px;
  }
  .plan-card {
    position: absolute; left: 518px; width: 210px; height: 80px;
    background: var(--white); border: 2px solid; border-radius: 10px;
    text-align: center; padding-left: 24px;
  }
  .plan-card--essential { top: 516px; border-color: var(--essential); }
  .plan-card--basic { top: 622px; border-color: var(--basic); }
  .plan-card--premier { top: 728px; border-color: var(--premier); }
  .plan-speed { display: block; margin-top: 10px; font-family: "Arimo", sans-serif; font-weight: 700; font-size: 26px; color: #111; }
  .plan-price { display: block; margin-top: 2px; font-family: "Oswald", sans-serif; font-size: 14px; color: var(--price-grey); }
  .plan-shield { position: absolute; left: 442px; width: 84px; height: 100px; }
  .plan-shield text { font-family: "Arimo", sans-serif; font-weight: 700; font-size: 13px; fill: #111; }

  .city-photo {
    position: absolute; left: 0; top: 714px; width: 768px; height: 366px;
    background:
      radial-gradient(ellipse 300px 60px at 50% 92%, rgba(230,150,60,.35), transparent 70%),
      radial-gradient(ellipse 380px 120px at 40% 60%, rgba(60,120,200,.25), transparent 70%),
      linear-gradient(180deg, #0a1a2e 0%, #142236 40%, #2a2a2c 80%, var(--city-deep) 100%);
  }
  .more-packages {
    position: absolute; left: 440px; top: 804px; width: 314px; text-align: center;
    color: var(--white); font-family: "Arimo", sans-serif; font-weight: 700;
    font-size: 13px; line-height: 24px; letter-spacing: .3px;
  }
  .more-packages span { display: block; }
  .more-packages span + span { margin-top: 25px; }

  .call-now {
    position: absolute; left: 124px; top: 932px; color: var(--white);
    font-family: "Archivo Black", sans-serif; font-size: 46px; line-height: 50px; letter-spacing: 12px;
  }
  .call-divider { position: absolute; left: 303px; top: 928px; width: 9px; height: 112px; background: var(--brand-green); }
  .phone {
    position: absolute; left: 327px; top: 952px; color: var(--white);
    font-family: "Arimo", sans-serif; font-weight: 700; font-size: 52px; letter-spacing: .5px;
  }

  .footer { position: absolute; left: 0; top: 1080px; width: 768px; height: 120px; background: var(--white); }
  .brand-dot { position: absolute; left: 22px; top: 14px; width: 86px; height: 86px; border-radius: 50%; background: var(--brand-blue); }
  .brand-name { position: absolute; left: 124px; top: 36px; color: var(--brand-blue); font-size: 29px; font-weight: 400; }
  .brand-tagline { position: absolute; right: 16px; top: 90px; color: var(--ink-dark); font-style: italic; font-size: 14px; }
</style>
</head>
<body>
<main class="ad">
  <svg width="0" height="0" style="position:absolute" aria-hidden="true">
    <defs>
      <linearGradient id="silver" x1="0" y1="0" x2="1" y2="1">
        <stop offset="0" stop-color="#f4f4f4"/><stop offset=".5" stop-color="#a9a9a9"/><stop offset="1" stop-color="#e6e6e6"/>
      </linearGradient>
      <linearGradient id="fill-essential" x1="0" y1="0" x2="0" y2="1">
        <stop offset="0" stop-color="#ffd23a"/><stop offset=".55" stop-color="#f08a1c"/><stop offset="1" stop-color="#d2401a"/>
      </linearGradient>
      <linearGradient id="fill-basic" x1="0" y1="0" x2="0" y2="1">
        <stop offset="0" stop-color="#e5f28a"/><stop offset=".55" stop-color="#8cc63f"/><stop offset="1" stop-color="#3f8d1f"/>
      </linearGradient>
      <linearGradient id="fill-premier" x1="0" y1="0" x2="0" y2="1">
        <stop offset="0" stop-color="#f2a8e6"/><stop offset=".55" stop-color="#c04fbf"/><stop offset="1" stop-color="#7a1f86"/>
      </linearGradient>
      <radialGradient id="tick-green" cx=".4" cy=".3" r=".8">
        <stop offset="0" stop-color="#9be85a"/><stop offset=".6" stop-color="#36a51a"/><stop offset="1" stop-color="#1d6e0c"/>
      </radialGradient>
    </defs>
  </svg>

  <div class="hero-photo" role="img" aria-label="Glowing blue fibre-optic strands on a dark background"></div>
  <h1 class="headline">Ultra High<br>Speed Internet</h1>
  <svg class="chevrons-red" viewBox="0 0 96 64" aria-hidden="true">
    <path d="M4 2 H26 L50 32 L26 62 H4 L28 32 Z" fill="#c8391e" opacity=".9"/>
    <path d="M40 2 H62 L86 32 L62 62 H40 L64 32 Z" fill="#e0562a" opacity=".8"/>
  </svg>
  <svg class="chevrons-light" viewBox="0 0 230 56" fill="none" stroke="rgba(190,225,255,.75)" stroke-width="3" aria-hidden="true">
    <path d="M6 4 H36 L58 28 L36 52 H6 L28 28 Z"/>
    <path d="M62 4 H92 L114 28 L92 52 H62 L84 28 Z"/>
    <path d="M118 4 H148 L170 28 L148 52 H118 L140 28 Z"/>
    <path d="M174 4 H204 L226 28 L204 52 H174 L196 28 Z"/>
  </svg>

  <div class="middle-band"></div>
  <div class="people-photo" role="img" aria-label="People gathered around a wooden table using laptops and phones"></div>

  <svg class="tick-badge" viewBox="0 0 174 174" aria-hidden="true">
    <circle cx="87" cy="87" r="84" fill="url(#silver)"/>
    <circle cx="87" cy="87" r="72" fill="#d9d9d9"/>
    <circle cx="87" cy="87" r="66" fill="url(#tick-green)"/>
    <path d="M52 90 L76 114 L124 58" fill="none" stroke="#ffffff" stroke-width="16" stroke-linecap="round" stroke-linejoin="round"/>
  </svg>
  <p class="tagline-hero">Truly Fast &amp; Reliable</p>

  <ul class="benefit-list">
    <li>Fast web browsing</li>
    <li>Real customer support</li>
    <li>Gaming without the lag</li>
    <li>Wall to wall WiFi coverage</li>
    <li>Simple and easy to read bills</li>
    <li>Less buffering while streaming</li>
    <li>No introductory charges, one constant rate</li>
  </ul>

  <h2 class="package-title">INTERNET SERVICE<br>PACKAGE</h2>

  <div class="plan-card plan-card--essential"><span class="plan-speed">50 MBPS</span><span class="plan-price">$50 Per Month</span></div>
  <svg class="plan-shield" style="top:504px" viewBox="0 0 84 100" aria-hidden="true">
    <path d="M42 2 L80 14 C80 52 68 80 42 98 C16 80 4 52 4 14 Z" fill="url(#silver)"/>
    <path d="M42 10 L72 20 C72 50 62 72 42 88 C22 72 12 50 12 20 Z" fill="url(#fill-essential)"/>
    <text x="42" y="44" text-anchor="middle">Essential</text>
  </svg>

  <div class="plan-card plan-card--basic"><span class="plan-speed">75 MBPS</span><span class="plan-price">$75 Per Month</span></div>
  <svg class="plan-shield" style="top:610px" viewBox="0 0 84 100" aria-hidden="true">
    <path d="M42 2 L80 14 C80 52 68 80 42 98 C16 80 4 52 4 14 Z" fill="url(#silver)"/>
    <path d="M42 10 L72 20 C72 50 62 72 42 88 C22 72 12 50 12 20 Z" fill="url(#fill-basic)"/>
    <text x="42" y="44" text-anchor="middle">Basic</text>
  </svg>

  <div class="city-photo" role="img" aria-label="Night city skyline with glowing network connection arcs"></div>

  <div class="plan-card plan-card--premier"><span class="plan-speed">100 MBPS</span><span class="plan-price">$100 Per Month</span></div>
  <svg class="plan-shield" style="top:716px" viewBox="0 0 84 100" aria-hidden="true">
    <path d="M42 2 L80 14 C80 52 68 80 42 98 C16 80 4 52 4 14 Z" fill="url(#silver)"/>
    <path d="M42 10 L72 20 C72 50 62 72 42 88 C22 72 12 50 12 20 Z" fill="url(#fill-premier)"/>
    <text x="42" y="44" text-anchor="middle">Premier</text>
  </svg>

  <p class="more-packages"><span>More flexible package:</span><span>www.brimcore-networks.example</span></p>

  <p class="call-now">CALL<br>NOW</p>
  <div class="call-divider"></div>
  <p class="phone">844-555-0173</p>

  <footer class="footer">
    <div class="brand-dot"></div>
    <p class="brand-name">Brimcore Networks</p>
    <p class="brand-tagline">“Fast and reliable internet service designed and catered to meet your needs”</p>
  </footer>
</main>
</body>
</html>
```